| Pairlocket | ||
| "Lanternmade Insurance" (this tagline includes the mathmatic "squared" symbol-see logo #161 winner) | ||
| Use fonts in logo. However, we may provide other direction on fonts for Address/Phone Numbers, etc. | ||
Cutting-Edge Modern Bright & Fun-filled |
| Dana R. Whitlock, MBA | ||
| Agency Principal | ||
| To Be Determined | ||
| TBD | ||
| dana@trypairlocket.com | ||
| www.trypairlocket.com | ||
1. We will need business cards for 2 people, Dana Whitlock (info provided above) and Morgan Whitlock...info as follows: Morgan P. Whitlock, MBA Agency Principal morgan@trypairlocket.com cell: 555.204.7316 2. Designer has provided final files to Mark Studio Hive. #161 was selected as Winner. This design has multiple components, please note. 3. Our logo style and design is somewhat "Retro" and cool, hip. We are in the insurance industry but definitely want to achieve a different "non-standard" look and feel. 4. Read Logo Brief for more information about the style of the two (twin brothers) Agency Principals. |
We are thinking that the "bottle cap" portion of our logo along with the "Pairlocket" portion would look good on the back of the business card. The bottle cap portion taking up most of the back of the card. Would like various options for the back. |
Download project material |
| pairlocket_17707.pdf |
| 1_17708.ai |
| Oak_Cellar_Depot_Business_Card_1_17709.jpg Pairlocket - Bus Card - example card design. We would like to see a style similar to this. |
| Brisk_Kettle_Business_Card_Example_17710.jpg Pairlocket - Bus Card - example card design. We would like to see a style similar to this. |

```html
<!DOCTYPE html>
<html lang="en">
<head>
<meta charset="utf-8">
<title>Pairlocket Stationery</title>
<link href="https://fonts.googleapis.com/css2?family=Raleway:wght@500;700&family=Open+Sans:wght@400;600&display=swap" rel="stylesheet">
<style>
:root{
  --green:#4f9a3a;
  --green-light:#8cc26d;
  --navy:#1f5a8a;
  --paper:#ffffff;
  --stage:#ece7df;
  --ink:#4a4a4a;
  --muted:#8f8f8f;
  --faint:#eef3ec;
}
*{margin:0;padding:0;box-sizing:border-box}
html,body{width:1200px;height:382px;overflow:hidden}
body{background:var(--stage);position:relative;font-family:"Open Sans",sans-serif;color:var(--ink)}
.brand{position:absolute;font-family:"Raleway",sans-serif;font-weight:700;color:var(--green);line-height:1;white-space:nowrap}
.brand-dot{display:inline-block;border-radius:50%;background:var(--navy);vertical-align:top}
.hero{position:absolute;left:36px;top:42px}
.hero .brand{position:static;font-size:44px}
.hero .brand-dot{width:13px;height:13px;margin-left:4px}
.hero .tagline{font-family:"Raleway",sans-serif;font-weight:500;font-size:11px;letter-spacing:2px;color:var(--green-light);margin-top:6px;text-transform:uppercase}
.hero .note{font-size:8px;color:var(--muted);margin-top:5px;margin-left:110px}
.piece{position:absolute;background:var(--paper);box-shadow:0 2px 5px rgba(0,0,0,.18);overflow:hidden}
.caption{position:absolute;font-size:7px;line-height:1;color:var(--muted);white-space:nowrap}
.card{width:140px;height:64px}
.card .brand{font-size:13px}
.card .small{position:absolute;font-size:4.5px;line-height:1.5;color:var(--ink);white-space:nowrap}
.card .name{font-weight:600;font-size:5.5px}
.card-green{background:var(--green)}
.card-green .brand{color:#fff}
.bar{position:absolute;background:var(--green)}
.letterhead{width:250px;height:326px}
.letterhead .side{position:absolute;left:0;top:0;bottom:0;width:8px;background:linear-gradient(var(--green),var(--navy))}
.letterhead .brand{left:24px;top:22px;font-size:18px}
.letterhead .contact{position:absolute;right:16px;top:18px;font-size:5px;line-height:1.6;text-align:right}
.letterhead .faint{position:absolute;left:65px;top:110px;width:120px;height:120px;border-radius:50%;background:var(--faint)}
.letterhead .foot{position:absolute;left:24px;right:16px;bottom:12px;border-top:1px solid var(--green-light);padding-top:3px;font-size:4.5px;color:var(--muted);text-align:center}
.envelope .brand{font-size:12px}
.envelope .addr{position:absolute;font-size:5px;line-height:1.5;white-space:nowrap}
</style>
</head>
<body>

<div class="hero">
  <div class="brand">Pairlocket<span class="brand-dot"></span></div>
  <div class="tagline">Lanternmade Insurance</div>
  <div class="note">Stationery Concepts</div>
</div>

<!-- Business cards -->
<div class="piece card" style="left:20px;top:160px">
  <div class="brand" style="left:12px;top:24px">Pairlocket</div>
  <div class="bar" style="left:0;right:0;bottom:0;height:4px"></div>
</div>
<div class="caption" style="left:20px;top:228px">Business Card Front</div>

<div class="piece card" style="left:168px;top:160px">
  <div class="bar" style="left:0;top:0;bottom:0;width:4px"></div>
  <div class="small" style="left:62px;top:8px"><div class="name">Dana R. Whitlock, MBA</div>Agency Principal<br>dana@trypairlocket.com<br>www.trypairlocket.com</div>
  <div class="brand" style="left:12px;top:46px;font-size:9px">Pairlocket</div>
</div>
<div class="caption" style="left:168px;top:228px">Business Card Back</div>

<div class="piece card card-green" style="left:20px;top:244px">
  <div class="brand" style="left:16px;top:24px">Pairlocket</div>
</div>
<div class="caption" style="left:20px;top:312px">Business Card Option Two</div>

<div class="piece card" style="left:168px;top:244px">
  <div class="bar" style="left:0;right:0;top:0;height:4px;background:var(--navy)"></div>
  <div class="small" style="left:10px;top:10px"><div class="name">Morgan P. Whitlock, MBA</div>Agency Principal<br>morgan@trypairlocket.com<br>cell: 555.204.7316</div>
  <div class="brand" style="left:92px;top:48px;font-size:9px">Pairlocket</div>
</div>
<div class="caption" style="left:168px;top:312px">Business Card Reverse</div>

<!-- Letterheads -->
<div class="piece letterhead" style="left:336px;top:20px">
  <div class="side"></div>
  <div class="brand">Pairlocket</div>
  <div class="contact">555.204.7316<br>dana@trypairlocket.com<br>www.trypairlocket.com</div>
  <div class="faint" aria-hidden="true"></div>
  <div class="foot">www.trypairlocket.com</div>
</div>
<div class="caption" style="left:426px;top:354px">Letterhead Option One</div>

<div class="piece letterhead" style="left:600px;top:20px">
  <div class="side" style="background:var(--green)"></div>
  <div class="brand">Pairlocket</div>
  <div class="contact">555.204.7316<br>morgan@trypairlocket.com<br>www.trypairlocket.com</div>
  <div class="faint" aria-hidden="true"></div>
  <div class="foot">www.trypairlocket.com</div>
</div>
<div class="caption" style="left:690px;top:354px">Letterhead Option Two</div>

<!-- Envelopes -->
<div class="piece envelope" style="left:876px;top:20px;width:300px;height:100px">
  <svg width="300" height="100" style="position:absolute;left:0;top:0" aria-hidden="true">
    <polygon points="0,0 300,0 300,28 150,56 0,28" fill="var(--navy)"/>
    <polygon points="0,28 150,56 300,28 300,34 150,62 0,34" fill="var(--green)"/>
    <circle cx="150" cy="36" r="6" fill="#fff"/>
  </svg>
  <div class="brand" style="left:116px;top:74px">Pairlocket</div>
</div>

<div class="piece envelope" style="left:876px;top:128px;width:300px;height:72px">
  <div class="bar" style="left:0;right:0;top:0;height:4px"></div>
  <div class="brand" style="left:14px;top:14px">Pairlocket</div>
  <div class="addr" style="left:14px;top:30px">www.trypairlocket.com</div>
</div>

<div class="piece envelope" style="left:892px;top:208px;width:284px;height:80px">
  <div class="brand" style="left:120px;top:12px">Pairlocket</div>
  <div class="addr" style="left:120px;top:28px">555.204.7316</div>
  <div class="bar" style="left:0;right:0;bottom:0;height:4px;background:var(--navy)"></div>
</div>

<div class="piece envelope" style="left:860px;top:262px;width:170px;height:74px">
  <div class="bar" style="left:0;top:0;bottom:0;width:4px"></div>
  <div class="brand" style="left:12px;top:12px;font-size:10px">Pairlocket</div>
  <div class="addr" style="left:12px;top:26px">Lanternmade Insurance</div>
</div>
<div class="caption" style="left:1060px;top:300px">Envelope Options Shown</div>

</body>
</html>
```